Wordpress Design Project

Hi,

I would like a more modern colourful design doing for my website ZEP Lnk (www.ze%plnk.com - remove percentage). But I do still want to keep the same sort of colors, just maybe lighter. More interesting.

I want the inside pages to NOT all look the same with just boring text.

I want the site to look more appealing and maybe a new logo.
Updates

I would like to mention I would prefer to keep the same logo after rethinking it (possibly a slight refresh of the logo if you feel its a good idea) and the same color scheme as at present.

Saves us rebranding a lot of our apps, tools online ads etc.

Also I thought it is worth mentioning we have 2 parts to the site. The front end and the logged in area. It would be good if when making the front end you keep in mind the back end at http://p.ze%plnk.com (remove percentage). We can only edit this limitedly (can edit the entire footer, the logo and full CSS of it). Would be good if we could make sure the header and footer can be used on the back end as well maybe to make it match.

I also want layouts making not just for the homepage. Obviously every page will basically be the same but I don't want all the other pages to just be 'text' and no real layout.

You can see out main pages on the website at the moment, I want those other pages to be laid out nice and differently as well. For example the testimonials page could be more interesting with speech bubbles and pictures of each person (just use placeholders). The affiliates page could be a description and then a nice fancy list of features why to join etc. 

Nothing overly complicated but I think it makes the whole site seem a lot better.

Target Market(s)

Affiliate Marketing. International.

Requirements
Must have
• Needs to be more room for links across the navigation at the top, also sub menus (at present we have a lot of pages which are hidden deep within other pages).
Nice to have
• Lists of features for advertisers and affiliates on the homepage part.

Menu items and buttons have nice hover over effects.

I want to get across on our pages all the different unique features we have.

Maybe some kind of slider which has past offer logos in, just use example logos.

```html
<!DOCTYPE html>
<html lang="en">
<head>
<meta charset="utf-8">
<title>ZEP Lnk – International CPA Affiliate Network</title>
<link href="https://fonts.googleapis.com/css2?family=Mulish:wght@300;400;600;700&display=swap" rel="stylesheet">
<style>
:root{
  --orange:#f26a1b;
  --red:#e2461c;
  --blue:#1f8fe0;
  --ink:#333;
  --text:#444;
  --muted:#888;
  --line:#d9d9d9;
  --dark:#3a3a3a;
  --black:#1c1c1c;
}
*{box-sizing:border-box;margin:0;padding:0}
html,body{width:1200px;height:1102px;overflow:hidden;background:#fff}
body{position:relative;font-family:"Mulish",Arial,sans-serif;color:var(--text)}
.abs{position:absolute}

/* header */
.brand{left:222px;top:10px;display:flex;align-items:center;gap:8px}
.brand-dot{width:40px;height:40px;border-radius:50%;background:var(--orange)}
.brand-name{font-size:36px;font-weight:700;color:var(--ink);letter-spacing:1px;line-height:1}
.brand-tag{left:316px;top:54px;font-size:11px;color:#555;letter-spacing:.2px}
.auth{left:752px;top:17px;display:flex;gap:4px}
.auth a{display:block;font-size:9px;font-weight:700;color:#fff;text-decoration:none;padding:3px 14px;border-radius:9px}
.auth .signin{background:var(--blue)}
.auth .signup{background:var(--orange)}
.social{display:flex;gap:10px}
.social span{width:21px;height:21px;border:1.5px solid #777;border-radius:50%;display:block}
.social-top{left:887px;top:16px}
.nav{left:227px;top:96px;display:flex;align-items:center;list-style:none}
.nav li{font-size:15px;color:#333;padding:6px 11px;margin-right:1px}
.nav li.active{background:var(--dark);color:#fff;border-radius:15px}

/* hero */
.hero{left:0;top:138px;width:1200px;height:320px;
  background:radial-gradient(circle at 12% 30%,#f4e4d4 0,rgba(244,228,212,0) 22%),
  radial-gradient(circle at 80% 40%,#f2a15c 0,rgba(242,161,92,0) 30%),
  linear-gradient(90deg,#d8b49a 0%,#c96a38 35%,#c0501e 60%,#b8461a 100%)}
.hero-title{left:0;top:203px;width:1190px;text-align:center;font-size:53px;font-weight:300;color:#fff;letter-spacing:1px}
.hero-pill{left:349px;top:272px;width:495px;height:54px;border-radius:27px;background:var(--orange);
  color:#fff;font-size:51px;font-weight:300;text-align:center;line-height:54px}
.dots{left:538px;top:420px;display:flex;gap:22px}
.dots span{width:15px;height:15px;border-radius:50%;border:3px solid rgba(255,255,255,.5)}

/* intro */
.band{left:0;top:585px;width:1200px;height:98px;background:linear-gradient(#fff,#e3e3e3);border-bottom:1px solid #ccc}
.intro-title{left:0;top:478px;width:1190px;text-align:center;font-size:24px;font-weight:400;color:var(--ink)}
.intro-text{left:247px;top:515px;width:690px;font-size:11px;line-height:15.5px;color:#333}
.join{left:493px;top:577px;width:204px;height:42px;border-radius:21px;background:var(--dark);
  color:#fff;font-size:20px;text-align:center;line-height:42px}

/* partners */
.partners{left:232px;top:655px;width:725px;height:99px;background:#fff;border:1px solid var(--line);border-radius:4px;box-shadow:0 1px 3px rgba(0,0,0,.1)}
.partners-tag{left:459px;top:645px;width:299px;height:16px;background:var(--orange);color:#fff;font-size:10.5px;text-align:center;line-height:16px;letter-spacing:.3px}
.partner-list{left:258px;top:692px;width:676px;display:flex;justify-content:space-between;align-items:center;font-size:17px;font-weight:600;color:#8a8a8a}
.arrow{width:22px;height:22px;border-radius:50%;background:#fff;border:1px solid #bbb;display:flex;align-items:center;justify-content:center}

/* news & testimonials */
.section-head{display:flex;align-items:center;gap:18px;font-size:22px;color:var(--ink)}
.view-all{background:var(--red);color:#fff;font-size:11px;padding:3px 14px;border-radius:2px}
.news-item{left:259px;display:flex;gap:32px}
.date{width:30px;height:30px;border:2px solid #555;text-align:center;font-size:13px;font-weight:700;line-height:14px;padding-top:2px;color:#333;flex:none}
.date small{display:block;font-size:5px;letter-spacing:1px;line-height:6px}
.news-text{font-size:9.5px;line-height:15.5px;color:#333;width:290px}
.quote{left:630px;width:300px;border:1px solid var(--line);border-radius:5px;padding:8px 14px 7px;font-size:9px;line-height:14px;color:#333;box-shadow:0 1px 2px rgba(0,0,0,.08)}
.quote cite{display:block;margin-top:6px;font-style:normal;font-weight:700;color:#888}

/* side tabs */
.tab{left:1166px;width:34px;border-radius:6px 0 0 6px;color:#fff;font-size:11px;font-weight:600;writing-mode:vertical-rl;transform:rotate(180deg);padding:10px 0;text-align:right}
.tab-login{top:87px;height:144px;background:var(--blue)}
.tab-social{top:241px;height:144px;background:var(--black)}

/* footer */
.footer{left:0;top:1033px;width:1200px;height:69px;background:linear-gradient(#eaeaea,#fff 30%);border-top:1px solid #ddd}
.footer-links{left:247px;top:1056px;font-size:9px;color:#888}
.copyright{left:247px;top:1080px;font-size:9px;color:#444}
.social-foot{left:681px;top:1060px}
.brand-foot{left:780px;top:1052px;display:flex;align-items:center;gap:7px}
.brand-foot .brand-dot{width:34px;height:34px}
.brand-foot .brand-name{font-size:30px}
</style>
</head>
<body>

<header>
  <div class="abs brand"><span class="brand-dot"></span><span class="brand-name">ZEP LNK</span></div>
  <div class="abs brand-tag">EARN MONEY &amp; INCREASE SALES</div>
  <div class="abs auth"><a class="signin">Sign In</a><a class="signup">Sign Up</a></div>
  <div class="abs social social-top" aria-label="Social links"><span></span><span></span><span></span></div>
  <ul class="abs nav">
    <li class="active">HOME</li><li>ABOUT US</li><li>OUR BLOG</li><li>TESTIMONIALS</li>
    <li>AFFILIATES</li><li>ADVERTISERS</li><li>CONTACT US</li>
  </ul>
</header>

<section>
  <div class="abs hero" role="img" aria-label="Blurred warm orange shopping street photograph"></div>
  <div class="abs hero-title">EARN MONEY</div>
  <div class="abs hero-pill">&amp; INCREASE SALES</div>
  <div class="abs dots">
    <span style="background:#e8413c"></span><span style="background:#3d8fe0"></span>
    <span style="background:#4cb84a"></span><span style="background:#f2b619"></span>
  </div>
</section>

<section>
  <div class="abs band"></div>
  <h1 class="abs intro-title">ZEP Lnk: International CPA Affiliate Network</h1>
  <p class="abs intro-text">Welcome to the ZEP Lnk affiliate network. On time payments, hot &amp; exclusive CPL/CPA offers, fast support and low fees for advertisers, is the making of a leading affiliate network!<br>ZEP Lnk offer a wide range of advertisers for your websites. So you can start monetizing your traffic or get an additional revenue stream, today</p>
  <div class="abs join">JOIN US TODAY!</div>
</section>

<section>
  <div class="abs partners"></div>
  <div class="abs partners-tag">USED BY THOUSANDS OF BIG SMALL BUSINESSES</div>
  <div class="abs partner-list">
    <span>Northwind</span><span>Brisa</span><span>Calder</span><span>Vela</span><span>Oakline</span><span>Juno</span><span>Tidewell</span><span>Marlo</span>
  </div>
  <div class="abs arrow" style="left:238px;top:726px"><svg width="8" height="10"><path d="M6 1L2 5l4 4" stroke="#222" stroke-width="2" fill="none"/></svg></div>
  <div class="abs arrow" style="left:928px;top:726px"><svg width="8" height="10"><path d="M2 1l4 4-4 4" stroke="#222" stroke-width="2" fill="none"/></svg></div>
</section>

<section>
  <div class="abs section-head" style="left:259px;top:783px">
    <svg width="40" height="38"><rect x="1" y="1" width="36" height="36" fill="none" stroke="#555" stroke-width="2"/><path d="M8 9h10v8H8zM22 10h9M22 15h9M8 22h23M8 27h23M8 32h23" stroke="#555" stroke-width="2" fill="none"/></svg>
    <span>NEWS / EVENT</span><span class="view-all" style="margin-left:22px">View All</span>
  </div>
  <div class="abs news-item" style="top:850px"><div class="date">20<small>FEB</small></div><p class="news-text">Lorem ipsum dolor sit amet, consectetuer adipiscing elit, sed diam nonummy nibh euismod tincidunt ut laoreet dolore magna.</p></div>
  <div class="abs news-item" style="top:904px"><div class="date">20<small>FEB</small></div><p class="news-text" style="width:300px">Lorem ipsum dolor sit amet, consectetuer adipiscing elit, sed diam nonummy nibh euismod tincidunt ut laoreet dolore magna.</p></div>
  <div class="abs news-item" style="top:953px"><div class="date">20<small>FEB</small></div><p class="news-text">Lorem ipsum dolor sit amet, consectetuer adipiscing elit, sed diam nonummy nibh euismod tincidunt ut laoreet dolore magna.</p></div>

  <div class="abs section-head" style="left:623px;top:783px">
    <svg width="40" height="38"><path d="M6 32l4-10L30 2l6 6-20 20z M10 22l6 6" stroke="#555" stroke-width="2" fill="none"/></svg>
    <span>TESTIMONIALS</span><span class="view-all" style="margin-left:20px">View All</span>
  </div>
  <blockquote class="abs quote" style="top:836px">"Lorem ipsum dolor sit amet, consectetuer adipiscing elit, sed diam nonummy nibh euismod tincidunt ut laoreet dolore magna."<cite>— Daniel Hart</cite></blockquote>
  <blockquote class="abs quote" style="top:924px">"Lorem ipsum dolor sit amet, consectetuer adipiscing elit, sed diam nonummy nibh euismod tincidunt ut laoreet dolore magna."<cite>— Daniel Hart</cite></blockquote>
</section>

<aside>
  <div class="abs tab tab-login">ACCOUNT LOGIN</div>
  <div class="abs tab tab-social">SOCIAL BAR</div>
</aside>

<footer>
  <div class="abs footer"></div>
  <div class="abs footer-links">Affiliate Terms &amp; Conditions | advertiser Terms &amp; Conditions | privacy Policy &amp; Cookies | faq | contact Us</div>
  <div class="abs copyright">© 2013 ZEP Media UK Ltd - All Rights Reserved.</div>
  <div class="abs social social-foot"><span></span><span></span><span></span></div>
  <div class="abs brand-foot"><span class="brand-dot"></span><span class="brand-name">ZEP LNK</span></div>
</footer>

</body>
</html>
```